Letterhead for Law Firm - Logo already prepared

I previously used to prepare a logo which I was quite pleased with, a copy is attached for your reference. I would like the font of the logo to be all the same size, rather than the 'S' and 'L' being larger than the other letters.
I have copies of the attached in other formats if necessary.
I need a letterhead prepared which is virtually identical to the draft attached, however I will be adding an address, phone number, fax number, mobile number and email. I will provide these details with whoever can assist me.
I will also be providing insurance details to be listed at the foot of the page.
Finally, I need the file to be supplied as a high resolution pdf with 2mm bleed.
If you require any further information, please do not hesitate to contact me.

```html
<!DOCTYPE html>
<html lang="en">
<head>
<meta charset="utf-8">
<title>Marwood Legal – Letterhead</title>
<link rel="stylesheet" href="https://fonts.googleapis.com/css2?family=Carlito:wght@400;700&display=swap">
<style>
  :root {
    --paper: #ffffff;
    --ink: #3b3b3b;
    --ink-soft: #4a4a4a;
    --accent: #f0642a;
    --accent-deep: #e2501c;
    --footer-top: #e4e4e4;
    --footer-bottom: #d2d2d2;
    --texture: #e9e9e9;
  }
  html, body {
    margin: 0;
    padding: 0;
    width: 848px;
    height: 1200px;
    overflow: hidden;
    background: var(--paper);
  }
  .letterhead {
    position: relative;
    width: 848px;
    height: 1200px;
    background: var(--paper);
    font-family: "Carlito", "Calibri", sans-serif;
    color: var(--ink);
    overflow: hidden;
  }
  .brand {
    position: absolute;
    top: 28px;
    right: 24px;
    display: flex;
    align-items: center;
    gap: 12px;
  }
  .brand-mark {
    width: 64px;
    height: 64px;
    border-radius: 50%;
    background: var(--accent);
  }
  .brand-name {
    font-size: 27px;
    font-weight: 400;
    letter-spacing: 1px;
    text-transform: uppercase;
    color: var(--ink);
  }
  .texture {
    position: absolute;
    left: 0;
    top: 300px;
    width: 848px;
    height: 826px;
  }
  .footer-rule {
    position: absolute;
    left: 0;
    top: 1126px;
    width: 848px;
    height: 2px;
    background: var(--accent-deep);
  }
  .footer {
    position: absolute;
    left: 0;
    top: 1128px;
    width: 848px;
    height: 72px;
    background: linear-gradient(to bottom, var(--footer-top), var(--footer-bottom));
    font-size: 18px;
    color: var(--ink-soft);
  }
  .footer-item {
    position: absolute;
    top: 27px;
    line-height: 20px;
    white-space: nowrap;
  }
  .footer-address { left: 16px; }
  .footer-phone { left: 434px; }
  .footer-web { left: 586px; }
  .footer-icon {
    display: inline-block;
    width: 20px;
    height: 20px;
    margin-right: 9px;
    border-radius: 50%;
    background: var(--accent);
    color: #fff;
    font-size: 12px;
    font-weight: 700;
    text-align: center;
    line-height: 20px;
    vertical-align: 0;
  }
</style>
</head>
<body>
  <div class="letterhead">
    <header class="brand">
      <span class="brand-mark"></span>
      <span class="brand-name">Marwood Legal</span>
    </header>

    <svg class="texture" role="img" aria-label="Soft grey halftone dot pattern sweeping across the lower left of the page" viewBox="0 0 848 826" preserveAspectRatio="none">
      <defs>
        <radialGradient id="texture-fade" cx="0.05" cy="0.95" r="0.95">
          <stop offset="0" stop-color="var(--texture)" stop-opacity="1"/>
          <stop offset="0.55" stop-color="var(--texture)" stop-opacity="0.6"/>
          <stop offset="1" stop-color="var(--texture)" stop-opacity="0"/>
        </radialGradient>
      </defs>
      <path d="M0 40 C 260 120, 560 380, 848 826 L 0 826 Z" fill="url(#texture-fade)"/>
    </svg>

    <div class="footer-rule"></div>
    <footer class="footer">
      <span class="footer-item footer-address">Address Line Here 1,&nbsp; Address Line Here 2 text he</span>
      <span class="footer-item footer-phone"><span class="footer-icon">P</span>555-014-2270</span>
      <span class="footer-item footer-web"><span class="footer-icon">W</span>www.marwoodlegal.com</span>
    </footer>
  </div>
</body>
</html>
```